Marrowgate Auctions Business Cards Design Needed

I need a business card design that is modern looking - double sided (maybe just my logo on the back, but open to suggestions) - the overall design is up to you. I want it to be easy to read - not over the top flashy. I already have a company logo which I uploaded so that needs to be used. The colors of my logo are the colors I want on the card... so blue and gray (do need to match the logo colors).

Requirements
Must have
• Would like the card to be sleek, modern and easy to ready

```html
<!DOCTYPE html>
<html lang="en">
<head>
<meta charset="utf-8">
<title>Marrowgate Auctions – Business Card Presentation</title>
<link rel="stylesheet" href="https://fonts.googleapis.com/css2?family=Questrial&display=swap">
<style>
  :root {
    --page: #ffffff;
    --ink-dark: #262626;
    --paper: #eceeef;
    --brand-blue: #1e73c8;
    --text-gray: #4a4a4a;
    --muted: #8c8c8c;
    --company-dim: #4f7aa6;
    --company-tag: #5f7a94;
  }
  * { box-sizing: border-box; margin: 0; padding: 0; }
  html, body { width: 1200px; height: 1200px; overflow: hidden; background: var(--page); }
  body { position: relative; font-family: "Questrial", sans-serif; color: var(--text-gray); }

  .card { position: absolute; width: 448px; height: 274px; background: var(--paper); overflow: hidden; }
  .card .band { position: absolute; left: 0; top: 0; width: 100%; background: var(--ink-dark); overflow: hidden; }
  .card .stripes { position: absolute; left: 0; top: 0; z-index: 0; }

  .card-front .band { height: 198px; }
  .card-front .brand {
    position: absolute; left: 0; width: 100%; top: 126px; z-index: 1;
    display: flex; justify-content: center; align-items: center; gap: 10px;
  }
  .card-front .brand-mark { width: 16px; height: 16px; background: var(--brand-blue); }
  .card-front .brand-name { font-size: 24px; color: var(--brand-blue); letter-spacing: 0.3px; }
  .card-front .tagline {
    position: absolute; top: 233px; width: 100%; text-align: center;
    font-size: 8px; color: var(--text-gray); letter-spacing: 0.3px;
  }

  .card-back .band { height: 75px; }
  .card-back .company { position: absolute; left: 61px; top: 30px; z-index: 1; font-size: 14px; color: var(--company-dim); letter-spacing: 0.5px; white-space: nowrap; }
  .card-back .company-tag { position: absolute; left: 61px; top: 50px; z-index: 1; font-size: 8px; color: var(--company-tag); letter-spacing: 0.3px; white-space: nowrap; }
  .card-back .person { position: absolute; left: 60px; top: 124px; font-size: 35px; font-weight: 700; color: var(--text-gray); line-height: 1; white-space: nowrap; }
  .card-back .role { position: absolute; left: 61px; top: 162px; font-size: 22px; color: var(--text-gray); line-height: 1; }
  .card-back .rule { position: absolute; left: 58px; top: 198px; width: 98px; height: 1px; background: #c4c6c8; }
  .card-back .contacts { position: absolute; left: 58px; top: 203px; list-style: none; }
  .card-back .contacts li { display: flex; align-items: center; gap: 5px; font-size: 8.5px; color: var(--text-gray); height: 16px; white-space: nowrap; }
  .card-back .contacts svg { width: 8px; height: 8px; fill: var(--text-gray); }

  .large-front { left: 128px; top: 427px; }
  .large-back { left: 624px; top: 427px; }
  .small { transform: scale(0.475); transform-origin: 0 0; }
  .small-front { left: 624px; top: 99px; }
  .small-back { left: 859px; top: 99px; }

  .brief-logo { position: absolute; left: 128px; top: 920px; display: flex; align-items: center; gap: 8px; }
  .brief-logo .brand-mark { width: 16px; height: 16px; background: var(--brand-blue); }
  .brief-logo .brand-name { font-size: 22px; color: var(--brand-blue); }

  .brief-text { position: absolute; left: 128px; top: 970px; width: 470px; font-size: 7.5px; line-height: 10px; color: var(--muted); }
  .brief-details { position: absolute; left: 128px; top: 1040px; font-size: 7.5px; line-height: 10px; color: var(--muted); list-style: none; }
</style>
</head>
<body>

<svg width="0" height="0" style="position:absolute">
  <defs>
    <linearGradient id="stripe-fade" x1="1" y1="0" x2="0" y2="1">
      <stop offset="0" stop-color="#4fa3d8" stop-opacity="0.95"/>
      <stop offset="0.55" stop-color="#2f6f9e" stop-opacity="0.45"/>
      <stop offset="1" stop-color="#262626" stop-opacity="0"/>
    </linearGradient>
    <linearGradient id="stripe-soft" x1="1" y1="0" x2="0" y2="1">
      <stop offset="0" stop-color="#4fa3d8" stop-opacity="0.55"/>
      <stop offset="0.6" stop-color="#2f6f9e" stop-opacity="0.2"/>
      <stop offset="1" stop-color="#262626" stop-opacity="0"/>
    </linearGradient>
  </defs>
</svg>

<!-- Front, small -->
<section class="card card-front small small-front">
  <div class="band">
    <svg class="stripes" width="448" height="198" viewBox="0 0 448 198">
      <polygon points="396,0 408,0 352,96 340,96" fill="url(#stripe-fade)"/>
      <polygon points="416,0 448,0 448,6 380,120 362,120" fill="url(#stripe-fade)"/>
      <polygon points="448,36 448,50 396,128 388,128" fill="url(#stripe-fade)"/>
    </svg>
    <div class="brand"><span class="brand-mark"></span><span class="brand-name">Marrowgate Auctions</span></div>
  </div>
  <p class="tagline">Improving Charity Auctions Nationwide</p>
</section>

<!-- Back, small -->
<section class="card card-back small small-back">
  <div class="band">
    <svg class="stripes" width="448" height="75" viewBox="0 0 448 75">
      <polygon points="150,0 164,0 118,75 104,75" fill="url(#stripe-soft)"/>
      <polygon points="172,0 196,0 150,75 128,75" fill="url(#stripe-soft)"/>
      <polygon points="204,0 212,0 166,75 158,75" fill="url(#stripe-soft)"/>
    </svg>
    <p class="company">Marrowgate Auctions, Inc</p>
    <p class="company-tag">Improving Charity Auctions Nationwide</p>
  </div>
  <p class="person">Elena Varga</p>
  <p class="role">President</p>
  <div class="rule"></div>
  <ul class="contacts">
    <li><svg viewBox="0 0 10 10"><path d="M2 0.5 L3.8 2.6 L2.9 3.7 Q4 6 6.3 7.1 L7.4 6.2 L9.5 8 L8.3 9.5 Q4 9 0.5 1.7 Z"/></svg>555 - 014 - 2290</li>
    <li><svg viewBox="0 0 10 10"><path d="M0.5 2 H9.5 V8 H0.5 Z M0.5 2 L5 5.5 L9.5 2"/></svg>marrowgateauctions@mail.com</li>
    <li><svg viewBox="0 0 10 10"><path d="M5 0.5 A4.5 4.5 0 1 0 5.01 0.5 Z M5 1.5 A3.5 3.5 0 1 1 4.99 1.5 Z"/></svg>http://bidharbor.com</li>
  </ul>
</section>

<!-- Front, large -->
<section class="card card-front large-front">
  <div class="band">
    <svg class="stripes" width="448" height="198" viewBox="0 0 448 198">
      <polygon points="396,0 408,0 352,96 340,96" fill="url(#stripe-fade)"/>
      <polygon points="416,0 448,0 448,6 380,120 362,120" fill="url(#stripe-fade)"/>
      <polygon points="448,36 448,50 396,128 388,128" fill="url(#stripe-fade)"/>
    </svg>
    <div class="brand"><span class="brand-mark"></span><span class="brand-name">Marrowgate Auctions</span></div>
  </div>
  <p class="tagline">Improving Charity Auctions Nationwide</p>
</section>

<!-- Back, large -->
<section class="card card-back large-back">
  <div class="band">
    <svg class="stripes" width="448" height="75" viewBox="0 0 448 75">
      <polygon points="150,0 164,0 118,75 104,75" fill="url(#stripe-soft)"/>
      <polygon points="172,0 196,0 150,75 128,75" fill="url(#stripe-soft)"/>
      <polygon points="204,0 212,0 166,75 158,75" fill="url(#stripe-soft)"/>
    </svg>
    <p class="company">Marrowgate Auctions, Inc</p>
    <p class="company-tag">Improving Charity Auctions Nationwide</p>
  </div>
  <p class="person">Elena Varga</p>
  <p class="role">President</p>
  <div class="rule"></div>
  <ul class="contacts">
    <li><svg viewBox="0 0 10 10"><path d="M2 0.5 L3.8 2.6 L2.9 3.7 Q4 6 6.3 7.1 L7.4 6.2 L9.5 8 L8.3 9.5 Q4 9 0.5 1.7 Z"/></svg>555 - 014 - 2290</li>
    <li><svg viewBox="0 0 10 10"><path d="M0.5 2 H9.5 V8 H0.5 Z M0.5 2 L5 5.5 L9.5 2"/></svg>marrowgateauctions@mail.com</li>
    <li><svg viewBox="0 0 10 10"><path d="M5 0.5 A4.5 4.5 0 1 0 5.01 0.5 Z M5 1.5 A3.5 3.5 0 1 1 4.99 1.5 Z"/></svg>http://bidharbor.com</li>
  </ul>
</section>

<!-- Brief summary -->
<div class="brief-logo"><span class="brand-mark"></span><span class="brand-name">Marrowgate Auctions</span></div>

<p class="brief-text">I need a business card design that is modern looking - double sided (maybe just my logo on the back, but open to suggestions) - the overall design is up to you. I want it to be easy to read - not over the top flashy. I already have a company logo which I uploaded so that needs to be used. The colors of my logo are the colors I want on the card... so blue and gray (do need to match the logo colors).</p>

<ul class="brief-details">
  <li>Name of Company: Marrowgate Auctions, Inc</li>
  <li>Name on Card: Elena Varga</li>
  <li>Title: Owner/President - Auctioneer</li>
  <li>Phone Number: 555-014-2290</li>
  <li>email: marrowgateauctions@mail.com</li>
  <li>Website: http://bidharbor.com/Tagline: Improving Charity Auctions Nationwide</li>
</ul>

</body>
</html>
```